Business card for builder specialising in renovations.

Need a card for our building business. Business name is under Martin Pelloe.
Have licence number on card ( 527916K)
Contact number (0400 382 615)
Want to work on logo for some business cards and shirts - something with MP or MPB or open to ideas??
No animations, No hammers. Something sharp and eye catching.
Highlight that we are a renovation specialist. Simple on front with extra details on back with some lines to jot down things.

Target Market(s)

Renovators

Industry/Entity Type

Building

Contact Information for Business Card

2 sided with room on back to jot things down.
Extra details on back so front can be simple ..like, renovations, bathrooms, decks, extensions, new builds,

Logo Text

MP

Font styles to use
Serif

Requirements
Must have
• Eye catching design .
• Name : Martin pelloe
• Licence number
• Contact number - 0400382615
Nice to have
• Some logo design that we can carry through to other forms of advertising
• Local builder
• Quality work
Should not have
• No animations

```html
<!DOCTYPE html>
<html lang="en">
<head>
<meta charset="UTF-8">
<title>Martin Pelloe – Business Card</title>
<link href="https://fonts.googleapis.com/css2?family=Playfair+Display:wght@400&family=Tinos:wght@400&display=swap" rel="stylesheet">
<style>
  :root {
    --stage: #2d2d2e;
    --card: #050505;
    --ink: #ffffff;
    --blue: #1b74c8;
  }
  * { box-sizing: border-box; margin: 0; padding: 0; }
  html, body { width: 1200px; height: 900px; overflow: hidden; background: var(--stage); }
  .stage { position: relative; width: 1200px; height: 900px; }

  .card {
    position: absolute;
    width: 620px; height: 354px;
    background: var(--card);
    border-radius: 22px;
    overflow: hidden;
    box-shadow: 0 18px 40px rgba(0,0,0,.45);
    color: var(--ink);
    font-family: "Tinos", "Times New Roman", serif;
  }
  .card--front { left: 70px; top: 80px; }
  .card--back  { left: 510px; top: 466px; }

  /* Brand name block */
  .brand { position: absolute; display: flex; align-items: center; gap: 16px; }
  .brand__square { width: 14px; height: 14px; background: var(--blue); flex: none; }
  .brand__name {
    font-family: "Playfair Display", Georgia, serif;
    font-weight: 400;
    color: var(--ink);
    text-transform: uppercase;
    line-height: .95;
    letter-spacing: .5px;
  }
  .card--front .brand { left: 200px; top: 92px; }
  .card--front .brand__name { font-size: 50px; }
  .card--back .brand { left: 44px; top: 92px; }
  .card--back .brand__name { font-size: 42px; }

  .web { position: absolute; font-size: 20px; letter-spacing: .3px; white-space: nowrap; }
  .accent { color: var(--blue); }
  .card--front .web { left: 330px; top: 212px; }

  .services {
    position: absolute; left: 40px; right: 30px; top: 280px;
    display: flex; align-items: center; gap: 10px;
    font-size: 15.5px; letter-spacing: .6px; text-transform: uppercase; white-space: nowrap;
  }
  .services .dot { width: 8px; height: 8px; background: var(--blue); flex: none; }

  .band { position: absolute; bottom: 0; left: 0; right: 0; height: 12px; }
  .band__light { position: absolute; left: 0; bottom: 0; width: 42%; height: 12px; background: var(--ink); }
  .band__blue  { position: absolute; right: 0; bottom: 0; width: 58%; height: 9px; background: var(--blue); }

  /* Back */
  .holder { position: absolute; right: 36px; top: 44px; text-align: right; }
  .holder__name {
    font-family: "Playfair Display", Georgia, serif;
    color: var(--blue); font-size: 24px; text-transform: uppercase; letter-spacing: .4px;
  }
  .holder__rule { position: absolute; right: -36px; top: 34px; width: 320px; height: 1.5px; background: var(--blue); }
  .holder__role { font-size: 13px; margin-top: 4px; }

  .licence { position: absolute; right: 36px; top: 150px; font-size: 16px; }
  .licence .label { color: var(--blue); }

  .divider { position: absolute; left: 0; right: 0; top: 228px; height: 1.5px; background: var(--blue); }

  .contacts { position: absolute; left: 64px; top: 244px; list-style: none; font-size: 17px; }
  .contacts li { display: flex; align-items: center; gap: 10px; height: 24px; white-space: nowrap; }
  .contacts svg { width: 13px; height: 13px; flex: none; }
</style>
</head>
<body>
<main class="stage">

  <section class="card card--front" aria-label="Card front">
    <div class="brand">
      <span class="brand__square"></span>
      <span class="brand__name">Martin<br>Pelloe</span>
    </div>
    <p class="web">www.<span class="accent">martinpelloe</span>.com</p>
    <p class="services">
      <span>Renovations</span><span class="dot"></span>
      <span>Bathrooms Decks</span><span class="dot"></span>
      <span>Extensions</span><span class="dot"></span>
      <span>New Builds</span>
    </p>
    <div class="band"><span class="band__light"></span><span class="band__blue"></span></div>
  </section>

  <section class="card card--back" aria-label="Card back">
    <div class="brand">
      <span class="brand__square"></span>
      <span class="brand__name">Martin<br>Pelloe</span>
    </div>

    <div class="holder">
      <p class="holder__name">Martin Pelloe</p>
      <span class="holder__rule"></span>
      <p class="holder__role">Director</p>
    </div>

    <p class="licence"><span class="label">Licence:</span> (527916K)</p>

    <span class="divider"></span>

    <ul class="contacts">
      <li>
        <svg viewBox="0 0 16 16" aria-hidden="true"><path fill="#1b74c8" d="M3.6 1.5l2.3 2.6-1.3 1.7c.8 1.8 2.2 3.2 4 4l1.7-1.3 2.6 2.3-1.3 2.3C6.6 13.4 2.6 9.4 1.3 4.4z"/></svg>
        <span>0400382615</span>
      </li>
      <li>
        <svg viewBox="0 0 16 16" aria-hidden="true"><rect x="1.5" y="3.5" width="13" height="9" fill="none" stroke="#1b74c8" stroke-width="1.5"/><path d="M1.5 3.5L8 9l6.5-5.5" fill="none" stroke="#1b74c8" stroke-width="1.5"/></svg>
        <span>info@martinpelloe.com</span>
      </li>
      <li>
        <svg viewBox="0 0 16 16" aria-hidden="true"><g fill="none" stroke="#1b74c8" stroke-width="1.3"><circle cx="8" cy="8" r="6.3"/><ellipse cx="8" cy="8" rx="2.8" ry="6.3"/><path d="M1.7 8h12.6M2.8 4.8h10.4M2.8 11.2h10.4"/></g></svg>
        <span>www.<span class="accent">martinpelloe</span>.com</span>
      </li>
    </ul>

    <div class="band"><span class="band__light"></span><span class="band__blue"></span></div>
  </section>

</main>
</body>
</html>
```